Ridgeline Orchards Organic Cherry POS card 7x11

We are wanting to create a one-sided 7 x 11 organic cherry card that is eye catching and informative.This should be clear and easy to read and not cluttered. We use these cards as a display in grocery stores, demo stands, and other events to market Organic Ridgeline Sweet Orchards. We have a few facts that we would like displayed on the card (see attachment).

Target Market(s)

Consumers

Industry/Entity Type

Agriculture

Requirements
Must have
• Natural color palettes
• Easy to read
• Ridgeline Orchards
Nice to have
• Unique, realistic cherry design

```html
<!DOCTYPE html>
<html lang="en">
<head>
<meta charset="utf-8">
<title>Ridgeline Orchards – Organic Cherry Card</title>
<link href="https://fonts.googleapis.com/css2?family=Archivo+Black&display=swap" rel="stylesheet">
<style>
  :root {
    --paper: #ffffff;
    --ink: #111111;
    --cherry-deep: #5e0a14;
    --cherry: #a3121f;
    --cherry-bright: #d42a36;
    --basket: #d9c08e;
  }
  html, body {
    margin: 0;
    padding: 0;
    overflow: hidden;
    background: var(--paper);
  }
  .card {
    position: relative;
    width: 764px;
    height: 1200px;
    overflow: hidden;
    background: var(--paper);
    font-family: "Archivo Black", "Arial Black", sans-serif;
    color: var(--ink);
  }
  .brand {
    position: absolute;
    left: 104px;
    top: 72px;
    display: flex;
    align-items: center;
    gap: 22px;
  }
  .brand-dot {
    width: 92px;
    height: 92px;
    border-radius: 50%;
    background: var(--cherry-deep);
    flex: none;
  }
  .brand-name {
    font-size: 46px;
    line-height: 1;
    color: var(--ink);
    white-space: nowrap;
  }
  .fact {
    position: absolute;
    left: 62px;
    margin: 0;
    font-size: 36px;
    line-height: 50px;
    font-weight: 400;
    white-space: nowrap;
    z-index: 2;
  }
  .fact-share { top: 255px; }
  .fact-state { top: 457px; }
  .benefits {
    position: absolute;
    left: 62px;
    top: 660px;
    margin: 0;
    padding: 0;
    list-style: none;
    font-size: 36px;
    line-height: 50px;
    white-space: nowrap;
    z-index: 2;
  }
  .cherry-photo {
    position: absolute;
    left: 247px;
    top: 856px;
    width: 497px;
    height: 290px;
    z-index: 1;
    background:
      radial-gradient(ellipse 40% 45% at 85% 30%, var(--basket) 0%, rgba(217,192,142,0) 100%),
      radial-gradient(ellipse 60% 55% at 55% 70%, var(--cherry-bright) 0%, var(--cherry) 45%, rgba(163,18,31,0) 100%),
      radial-gradient(ellipse 70% 60% at 60% 55%, var(--cherry-deep) 0%, rgba(94,10,20,0) 100%);
  }
</style>
</head>
<body>
  <main class="card">
    <header class="brand">
      <span class="brand-dot"></span>
      <span class="brand-name">Ridgeline Orchards</span>
    </header>

    <p class="fact fact-share">Organic Ridgeline cherries<br>make up 1/3 of the<br>nation’s production.</p>

    <p class="fact fact-state">Washington State is the<br>nation’s largest producer of<br>organic cherries.</p>

    <ul class="benefits">
      <li>Health benefits:</li>
      <li>Fat Free</li>
      <li>Source of Vitamin C</li>
      <li>A Natural Anti-Inflammatory</li>
      <li>Source of Potassium</li>
      <li>Source of Melatonin</li>
    </ul>

    <div class="cherry-photo" role="img" aria-label="Photo of fresh red sweet cherries with stems spilling from a woven basket"></div>
  </main>
</body>
</html>
```